Redesign the *Settings* screen for the BrelloZ app.

BrelloZ app is in production, but we need to refresh and redesign the settings screen to be cleaner, easier, more intuitive, and more professional looking.

Project Deadline Extended
Reason: Several designers have requested more time. This will also give time to provide feedback on existing designs.

Requirements
Must have
• Black background, so that the screen is consistent with the rest of the app.

```html
<!DOCTYPE html>
<html lang="en">
<head>
<meta charset="utf-8">
<title>BrelloZ – Settings</title>
<link href="https://fonts.googleapis.com/css2?family=Roboto:wght@400;500;700&display=swap" rel="stylesheet">
<style>
:root{
  --page:#14171b;
  --screen:#1b1b1b;
  --header:#1f1f1f;
  --card:#242424;
  --gap:#161616;
  --divider:#3a3a3a;
  --text:#ffffff;
  --muted:#8a8a8a;
  --dim:#5e5e5e;
  --accent:#ff9a0a;
  --toggle:#5cf55a;
  --toggle-track:#3f6b3c;
}
*{margin:0;padding:0;box-sizing:border-box}
html,body{width:949px;height:1200px;overflow:hidden;background:var(--page)}
body{font-family:"Roboto",Arial,sans-serif;color:var(--text);position:relative}
.screen{position:absolute;left:143px;top:13px;width:340px;height:602px;background:var(--screen);transform:scale(1.95);transform-origin:0 0;overflow:hidden}
.abs{position:absolute}
.status{top:0;left:0;width:340px;height:20px;font-size:10.5px;display:flex;align-items:center;justify-content:space-between;padding:0 7px}
.status .time{position:absolute;left:0;right:0;text-align:center}
.status-left,.status-right{display:flex;align-items:center;gap:4px;position:relative;z-index:1}
.nav{top:20px;left:0;width:340px;height:38px;background:var(--header);text-align:center;font-size:14.5px;line-height:38px}
.card{left:0;width:340px;background:var(--card)}
.card-title{position:absolute;left:27px;font-size:14px;font-weight:500}
.info{position:absolute;left:301px;width:18px;height:18px;border-radius:50%;background:#6a6a6a;color:#2a2a2a;font:italic 700 11px/18px Georgia,serif;text-align:center}
.divider{position:absolute;left:27px;right:0;height:1px;background:var(--divider)}
.icon-btn{position:absolute;width:31px;height:31px;border-radius:50%;border:1px solid #4a4a4a;display:flex;align-items:center;justify-content:center}
.icon-btn.active{background:var(--accent);border-color:var(--accent)}
.opt-label{position:absolute;font-size:12px;color:var(--muted)}
.opt-label.active{color:var(--text)}
.loc-label{position:absolute;width:60px;text-align:center;font-size:12px;color:var(--dim)}
.loc-label.active{color:var(--text)}
.toggle{position:absolute;left:284px;top:74px;width:36px;height:14px;border-radius:7px;background:var(--toggle-track)}
.toggle::after{content:"";position:absolute;right:-2px;top:-4px;width:21px;height:21px;border-radius:50%;background:var(--toggle)}
.actions{top:456px;left:0;width:340px;height:101px;background:var(--gap)}
.action-label{position:absolute;font-size:12.5px;line-height:13px;color:var(--dim)}
.action-label small{display:block;font-size:7.5px;line-height:10px}
.action-label.active{color:var(--text)}
.tabbar{top:557px;left:0;width:340px;height:45px;background:var(--header);border-top:1px solid #2b2b2b}
.tab{position:absolute;top:5px;width:60px;text-align:center;font-size:8.5px;color:var(--muted)}
.tab svg{display:block;margin:0 auto 2px}
.tab.active{color:var(--accent)}
</style>
</head>
<body>
<main class="screen">
  <div class="abs status">
    <div class="status-left">
      <svg width="30" height="6" viewBox="0 0 30 6"><g fill="#fff"><circle cx="3" cy="3" r="2.6"/><circle cx="9" cy="3" r="2.6"/><circle cx="15" cy="3" r="2.6"/></g><g fill="none" stroke="#fff" stroke-width=".8"><circle cx="21" cy="3" r="2.3"/><circle cx="27" cy="3" r="2.3"/></g></svg>
      <span>Plinth</span>
      <svg width="11" height="8" viewBox="0 0 11 8"><path d="M5.5 8 0 2.5a8 8 0 0 1 11 0Z" fill="#fff"/></svg>
    </div>
    <span class="time">9:41 AM</span>
    <div class="status-right">
      <svg width="6" height="10" viewBox="0 0 6 10" fill="none" stroke="#fff" stroke-width=".9"><path d="M1 2.5 5 7 3 9V1l2 2-4 4.5"/></svg>
      <span>42%</span>
      <svg width="22" height="10" viewBox="0 0 22 10"><rect x=".5" y=".5" width="19" height="9" rx="1.5" fill="none" stroke="#fff"/><rect x="2" y="2" width="7" height="6" fill="#fff"/><rect x="20.5" y="3" width="1.5" height="4" fill="#fff"/></svg>
    </div>
  </div>

  <header class="abs nav">Settings</header>

  <section class="abs card" style="top:58px;height:128px">
    <h2 class="card-title" style="top:24px">Device Mount Position</h2>
    <span class="info" style="top:24px">i</span>
    <div class="divider" style="top:57px"></div>
    <div class="icon-btn active" style="left:27px;top:75px">
      <svg width="16" height="16" viewBox="0 0 16 16" fill="none" stroke="#1b1b1b" stroke-width="1.4"><path d="M3 14C3 8 6 5 12 5M9 2l3 3-3 3"/></svg>
    </div>
    <span class="opt-label active" style="left:75px;top:84px">Forwards</span>
    <div class="icon-btn" style="left:181px;top:75px">
      <svg width="16" height="16" viewBox="0 0 16 16" fill="none" stroke="#5a5a5a" stroke-width="1.2"><path d="M13 14C13 8 10 5 4 5M7 2 4 5l3 3"/></svg>
    </div>
    <span class="opt-label" style="left:229px;top:84px">Backwards</span>
  </section>

  <section class="abs card" style="top:192px;height:147px">
    <h2 class="card-title" style="top:24px">Device Mount Location</h2>
    <span class="info" style="top:24px">i</span>
    <div class="divider" style="top:56px"></div>
    <div class="icon-btn" style="left:36px;top:75px"><svg width="12" height="12" viewBox="0 0 12 12" fill="none" stroke="#666" stroke-width="1.2"><path d="M2 2l4 4 4-4M2 6l4 4 4-4"/></svg></div>
    <div class="icon-btn active" style="left:125px;top:75px"><svg width="12" height="12" viewBox="0 0 12 12" fill="none" stroke="#1b1b1b" stroke-width="1.6"><path d="M2 6l4-4 4 4M2 10l4-4 4 4"/></svg></div>
    <div class="icon-btn" style="left:206px;top:75px"><svg width="12" height="12" viewBox="0 0 12 12" fill="none" stroke="#666" stroke-width="1.2"><path d="M6 2 2 6l4 4M10 2 6 6l4 4"/></svg></div>
    <div class="icon-btn" style="left:289px;top:75px"><svg width="12" height="12" viewBox="0 0 12 12" fill="none" stroke="#666" stroke-width="1.2"><path d="M2 2l4 4-4 4M6 2l4 4-4 4"/></svg></div>
    <span class="loc-label" style="left:21px;top:115px">Bottom</span>
    <span class="loc-label active" style="left:111px;top:115px">Top</span>
    <span class="loc-label" style="left:191px;top:115px">Left</span>
    <span class="loc-label" style="left:274px;top:115px">Right</span>
  </section>

  <section class="abs card" style="top:346px;height:110px">
    <h2 class="card-title" style="top:22px">Bullseye Mode</h2>
    <span class="info" style="top:22px">i</span>
    <div class="divider" style="top:55px"></div>
    <span class="abs" style="left:27px;top:75px;font-size:11.5px;font-weight:700">ON</span>
    <span class="toggle" role="switch" aria-checked="true"></span>
  </section>

  <section class="abs actions">
    <div class="icon-btn" style="left:26px;top:35px">
      <svg width="18" height="18" viewBox="0 0 18 18" fill="none" stroke="#555" stroke-width="1.2"><path d="M15 7a6.5 6.5 0 0 0-12-1M3 11a6.5 6.5 0 0 0 12 1M3 2v4h4M15 16v-4h-4"/></svg>
    </div>
    <span class="action-label" style="left:67px;top:45px">Sync<small>Account data</small></span>
    <div class="icon-btn active" style="left:131px;top:35px">
      <svg width="10" height="16" viewBox="0 0 10 16" fill="none" stroke="#1b1b1b" stroke-width="1.3"><path d="M1 4.5 8.5 11 5 14V2l3.5 3L1 11.5"/></svg>
    </div>
    <span class="action-label active" style="left:170px;top:45px">Bluetooth<small>Disconnect</small></span>
    <div class="icon-btn" style="left:241px;top:35px">
      <svg width="14" height="16" viewBox="0 0 14 16" fill="none" stroke="#555" stroke-width="1.2"><path d="M2 16V1M2 2h9L8 5.5 11 9H2"/></svg>
    </div>
    <span class="action-label" style="left:278px;top:45px">Report<small>Issue</small></span>
  </section>

  <nav class="abs tabbar">
    <div class="tab active" style="left:-5px">
      <svg width="24" height="24" viewBox="0 0 24 24" fill="none" stroke="#a8a8a8" stroke-width="1"><circle cx="12" cy="12" r="11"/><circle cx="12" cy="12" r="8"/><circle cx="12" cy="12" r="5"/></svg>Train</div>
    <div class="tab" style="left:88px">
      <svg width="24" height="24" viewBox="0 0 24 24" fill="none" stroke="#8a8a8a" stroke-width="1"><rect x="2" y="4" width="20" height="18" rx="1.5"/><path d="M2 9h20M7 2v4M17 2v4"/><g fill="#8a8a8a" stroke="none"><rect x="5" y="12" width="2" height="2"/><rect x="9" y="12" width="2" height="2"/><rect x="13" y="12" width="2" height="2"/><rect x="17" y="12" width="2" height="2"/><rect x="5" y="16" width="2" height="2"/><rect x="9" y="16" width="2" height="2"/><rect x="13" y="16" width="2" height="2"/></g></svg>History</div>
    <div class="tab" style="left:182px">
      <svg width="28" height="24" viewBox="0 0 28 24" fill="none" stroke="#8a8a8a" stroke-width="1"><path d="M1 8 14 2l13 6-13 6Z"/><path d="M7 11v6c4 3 10 3 14 0v-6M24 9v8"/></svg>Learn</div>
    <div class="tab" style="left:278px">
      <svg width="24" height="24" viewBox="0 0 24 24" fill="none" stroke="#8a8a8a" stroke-width="1"><circle cx="12" cy="12" r="4"/><path d="M12 1.5l2 3 3.4-1 .6 3.5 3.4 1.1-1.5 3.2 2 2.7-3.2 1.6.3 3.5-3.5-.3-1.6 3.2L12 19.5l-2.6 2.4-1.6-3.2-3.5.3.3-3.5L1.4 14l2-2.7L1.9 8.1 5.3 7l.6-3.5 3.4 1Z"/></svg>Settings</div>
  </nav>
</main>
</body>
</html>
```